small auto electrical company needs new logo and business cards !!!

we are a small auto electrical company (Corvanne Motors Ltd) that has been running for 13 years the logo we have was put together by dinosaurs so we are looking at re branding the company starting with business cards and a new logo we fit GPS tracking devices for young drivers through there insurance company also we fit hands free systems and dash cameras also safety locks to fleet vehicles we would like bright eye catching colours day glow and neon and quirky designs for the logo our original logo was baby blue which i have added a picture enclosed we would like double sided but have a space to write notes and prices preferably not white on back same colour throughout many thanks
Reason: Just a chance to finalise any designs we want CM logos or C logos - No 1st's and no dinosaurs lol
Industry/Entity Type
Business
Contact Information for Business Card
Installs@corvannemotors.co.uk
07700900482
www.Corvannemotors.co.uk
Logo Text
Corvanne Motors Ltd - Fleets and Insurance Services
Requirements
Must have
- new logo design !!
Nice to have
- Satellite in logo or something attaining to gps
- maybe a car in the logo
Should not have
- shouldnt have first as 1st it is CoRVANNE Motors

```html
<!DOCTYPE html>
<html lang="en">
<head>
<meta charset="utf-8">
<title>Corvanne Motors Ltd — Business Cards</title>
<link rel="stylesheet" href="https://fonts.googleapis.com/css2?family=Cinzel:wght@700&family=Cormorant+Garamond:ital,wght@1,600&family=Noto+Sans:ital,wght@0,400;1,700&display=swap">
<style>
  :root {
    --page: #e4e4e4;
    --teal: #00a896;
    --teal-glow: #12d6bf;
    --carbon-light: #2e2e2e;
    --carbon-dark: #121212;
    --band: #232323;
    --shadow-wedge: #0d0d0d;
    --white: #ffffff;
    --silver: #e6e6e6;
  }
  * { margin: 0; padding: 0; box-sizing: border-box; }
  html, body { width: 1200px; height: 1200px; overflow: hidden; background: var(--page); }
  .canvas { position: relative; width: 1200px; height: 1200px; }
  .card {
    position: absolute; left: 240px; width: 720px; height: 436px; overflow: hidden;
    box-shadow: 0 18px 30px rgba(0,0,0,.35);
  }
  .card--front { top: 106px; }
  .card--back { top: 630px; }
  .card__shapes { position: absolute; inset: 0; width: 100%; height: 100%; }
  .carbon { position: absolute; inset: 0; background: linear-gradient(160deg, var(--carbon-light) 0%, #1c1c1c 55%, var(--carbon-dark) 100%); }

  .wordmark { position: absolute; display: flex; align-items: center; gap: 12px; font-family: "Cinzel", serif; font-weight: 700; line-height: 1; }
  .wordmark__dot { width: 46px; height: 46px; border-radius: 50%; flex: none; }
  .wordmark__name { font-size: 46px; letter-spacing: 1px; }
  .wordmark__sub { font-size: 27px; letter-spacing: 1px; margin-top: 4px; }
  .wordmark--front { left: 48px; top: 66px; }
  .wordmark--front .wordmark__dot { background: var(--teal-glow); }
  .wordmark--front .wordmark__name { color: var(--teal-glow); }
  .wordmark--front .wordmark__sub { color: var(--silver); }
  .wordmark--back { left: 0; right: 0; top: 180px; justify-content: center; color: var(--white); }
  .wordmark--back .wordmark__dot { background: var(--white); }

  .person { position: absolute; right: 30px; text-align: right; font-family: "Noto Sans", sans-serif; color: var(--white); }
  .person__name { top: 114px; font-size: 32px; font-weight: 700; font-style: italic; letter-spacing: .5px; }
  .person__role { top: 168px; font-size: 21px; letter-spacing: .8px; }

  .contacts { position: absolute; right: 30px; top: 262px; list-style: none; font-family: "Noto Sans", sans-serif; color: var(--white); font-size: 17px; letter-spacing: .4px; }
  .contacts li { display: flex; align-items: center; justify-content: flex-end; gap: 16px; height: 28px; margin-bottom: 17px; white-space: nowrap; }
  .contacts svg { width: 29px; height: 29px; flex: none; }

  .services { position: absolute; left: 0; right: 0; top: 318px; text-align: center; color: var(--white); font-family: "Cormorant Garamond", serif; font-style: italic; font-weight: 600; text-transform: uppercase; }
  .services__title { font-size: 23px; letter-spacing: 1px; margin-bottom: 4px; }
  .services__line { font-size: 16px; letter-spacing: 1px; line-height: 22px; }
</style>
</head>
<body>
<main class="canvas">
  <section class="card card--front">
    <div class="carbon" role="img" aria-label="Dark carbon fibre weave texture"></div>
    <svg class="card__shapes" viewBox="0 0 900 545" preserveAspectRatio="none" aria-hidden="true">
      <polygon points="650,0 900,0 900,545 420,545" fill="var(--teal)"/>
      <polygon points="478,203 560,203 525,262" fill="var(--shadow-wedge)"/>
      <rect x="478" y="128" width="422" height="75" fill="var(--band)"/>
    </svg>
    <div class="wordmark wordmark--front">
      <span class="wordmark__dot"></span>
      <div><div class="wordmark__name">CORVANNE</div><div class="wordmark__sub">MOTORS LTD</div></div>
    </div>
    <h1 class="person person__name">Maren Holt</h1>
    <p class="person person__role">Project Manager</p>
    <ul class="contacts">
      <li>07700900482
        <svg viewBox="0 0 30 30"><circle cx="15" cy="15" r="14" fill="#fff"/><path d="M10.5 8.5l3 3-1.7 1.7c.9 1.9 2.2 3.3 4 4.1l1.7-1.7 3 3-2 2c-5 0-10-5-10-10z" fill="var(--teal)"/></svg>
      </li>
      <li>www.Corvannemotors.co.uk
        <svg viewBox="0 0 30 30"><circle cx="15" cy="15" r="14" fill="#fff"/><g fill="none" stroke="var(--teal)" stroke-width="1.4"><circle cx="15" cy="15" r="8"/><ellipse cx="15" cy="15" rx="3.5" ry="8"/><path d="M7 15h16M8.5 11h13M8.5 19h13"/></g></svg>
      </li>
      <li>Installs@corvannemotors.co.uk
        <svg viewBox="0 0 30 30"><circle cx="15" cy="15" r="14" fill="#fff"/><rect x="8" y="10" width="14" height="10" fill="var(--teal)"/><path d="M8 10l7 6 7-6M8 20l5-5M22 20l-5-5" fill="none" stroke="#fff" stroke-width="1.2"/></svg>
      </li>
    </ul>
  </section>

  <section class="card card--back">
    <div class="carbon" role="img" aria-label="Dark carbon fibre weave texture"></div>
    <div class="wordmark wordmark--back">
      <span class="wordmark__dot"></span>
      <div><div class="wordmark__name">CORVANNE</div><div class="wordmark__sub">MOTORS LTD</div></div>
    </div>
    <div class="services">
      <h2 class="services__title">Our Services</h2>
      <p class="services__line">GPS Tracking Devices - Hands Free Systems</p>
      <p class="services__line">Dash Cameras - Safety Locks to Fleet Vehicles</p>
    </div>
  </section>
</main>
</body>
</html>
```